Brookvale Holdings Ltd - Logo and Business Card

Create a logo and business card design for our new company.

Canadian private investment company with holdings in Saskatchewan Oil and real-estate.

Target Market(s)

Investors

Industry/Entity Type

Finance

Contact Information for Business Card

Name - Dominic Harlow
Position - President
Phone - 306.482.7159
Website - www.brookvaleholdings.ca

Logo Text

Today. Tomorrow. Together. (Tag Line)

Colors

Designer to choose colors to be used in the design.

Requirements
Must have
• Logo Must Have - Type Font only
• Must be modern, professional and stand out from the crowd.
Nice to have
• Don't have any, blank slate.

```html
<!DOCTYPE html>
<html lang="en">
<head>
<meta charset="utf-8">
<title>Brookvale Holdings Ltd – Business Card</title>
<link href="https://fonts.googleapis.com/css2?family=Open+Sans:wght@400&family=Tinos:wght@700&display=swap" rel="stylesheet">
<style>
  :root {
    --backdrop: #e9e7e3;
    --card-black: #060606;
    --card-white: #ffffff;
    --brand-red: #e0212b;
    --text-light: #ffffff;
    --shadow: rgba(0,0,0,0.18);
  }
  * { margin: 0; padding: 0; box-sizing: border-box; }
  html, body { width: 1200px; height: 902px; overflow: hidden; background: var(--backdrop); }
  .canvas { position: relative; width: 1200px; height: 902px; overflow: hidden; background: var(--backdrop); }
  .card {
    position: absolute; left: 100px; top: 166px; width: 1000px; height: 569px;
    border-radius: 26px; overflow: hidden; background: var(--card-white);
    box-shadow: 0 12px 36px var(--shadow);
  }
  .card-shapes { position: absolute; inset: 0; width: 1000px; height: 569px; }
  .holder-name {
    position: absolute; left: 48px; top: 66px;
    font-family: "Tinos", "Times New Roman", serif; font-weight: 700;
    font-size: 38px; line-height: 1; color: var(--brand-red);
  }
  .holder-title {
    position: absolute; left: 48px; top: 106px;
    font-family: "Open Sans", Arial, sans-serif; font-weight: 400;
    font-size: 25px; line-height: 1; color: var(--text-light);
  }
  .contact-list { position: absolute; left: 50px; top: 390px; list-style: none; }
  .contact-item {
    display: flex; align-items: center; height: 37px;
    font-family: "Open Sans", Arial, sans-serif; font-size: 25px; color: var(--text-light);
  }
  .contact-icon {
    width: 27px; height: 27px; border-radius: 5px; background: var(--brand-red);
    margin-right: 12px; flex: none; display: flex; align-items: center; justify-content: center;
  }
  .contact-icon svg { width: 19px; height: 19px; }
  .brand { position: absolute; left: 560px; top: 190px; width: 400px; text-align: center; }
  .brand-dot { width: 74px; height: 74px; border-radius: 50%; background: var(--brand-red); margin: 0 auto 46px; }
  .brand-name {
    font-family: "Tinos", "Times New Roman", serif; font-weight: 700;
    color: var(--brand-red); line-height: 1;
  }
  .brand-name .line-main { display: block; font-size: 46px; letter-spacing: 0.5px; }
  .brand-name .line-sub { display: block; font-size: 22px; letter-spacing: 1px; margin-top: 6px; }
</style>
</head>
<body>
<div class="canvas">
  <div class="card">
    <svg class="card-shapes" viewBox="0 0 1000 569" aria-hidden="true">
      <path d="M0 0 H537 Q409 284.5 537 569 H0 Z" fill="var(--card-black)"/>
      <path d="M548 0 Q420 284.5 540 569 L547 569 Q438 284.5 556 0 Z" fill="var(--brand-red)"/>
      <circle cx="0" cy="103" r="32" fill="var(--brand-red)"/>
    </svg>

    <div class="holder-name">Dominic Harlow</div>
    <div class="holder-title">President</div>

    <ul class="contact-list">
      <li class="contact-item">
        <span class="contact-icon">
          <svg viewBox="0 0 20 20"><rect x="6" y="2" width="8" height="16" rx="1.5" fill="none" stroke="#000" stroke-width="1.6"/><rect x="8" y="5" width="4" height="4" fill="#000"/><line x1="8" y1="12" x2="12" y2="12" stroke="#000" stroke-width="1.2"/><line x1="8" y1="14.5" x2="12" y2="14.5" stroke="#000" stroke-width="1.2"/></svg>
        </span>306.482.7159
      </li>
      <li class="contact-item">
        <span class="contact-icon">
          <svg viewBox="0 0 20 20"><rect x="2.5" y="5" width="15" height="10" fill="none" stroke="#000" stroke-width="1.6"/><path d="M2.5 5 L10 11 L17.5 5" fill="none" stroke="#000" stroke-width="1.6"/></svg>
        </span>info@brookvaleholdings.ca
      </li>
      <li class="contact-item">
        <span class="contact-icon">
          <svg viewBox="0 0 20 20"><circle cx="10" cy="10" r="7" fill="none" stroke="#000" stroke-width="1.5"/><ellipse cx="10" cy="10" rx="3" ry="7" fill="none" stroke="#000" stroke-width="1.2"/><line x1="3" y1="10" x2="17" y2="10" stroke="#000" stroke-width="1.2"/></svg>
        </span>www.brookvaleholdings.ca
      </li>
    </ul>

    <div class="brand">
      <div class="brand-dot"></div>
      <div class="brand-name">
        <span class="line-main">BROOKVALE</span>
        <span class="line-sub">HOLDINGS LTD</span>
      </div>
    </div>
  </div>
</div>
</body>
</html>
```